New Branding Business Card Design

Redesign business card according to new branding update.

** The design received so far are single color + BLACK.
I'd encourage designer to use different tones of blue / purple as described in the Designer Brief color palette

Target Market(s)

International

Industry/Entity Type

Medical Equipment

Contact Information for Business Card

Logo on one side (Designer can decide if they want to move certain info from the other side to save space)

Main body info (company name, individual name in both English and Chinese, contact info etc) on the other
Prefer a 'cleaner' layout - vs 'all over the place'
Prefer flush left alignment

Font styles to use
Sans Serif

Requirements
Must have
• Key info
• (Company name (English)): VORAM (HK) Limited
• (Name (English)): Marcus L. Pryde
• (Credential): FCPA, FHKSI
• (Title): Founder, Managing Director & CEO
• For the following info, designers decide whether to use colon or no colon, stroke separator, or use icon gfx for T (for telephone fixed line, M for mobile etc.)
• T: +852 3517 VORAM / +852 3517 4062
• M: +852 6243 7719 / + 86 139 2745 3186
• E: marcus.l.pryde@voram-example.hk
Nice to have
• Depending on the space and spacing available designers can add or use fuller title and other info
• Title: Chairman of the Executive Committee, Founder, Managing Director & CEO
• (Name (Chinese)): 林書恒
Should not have
• One of our business entities a long company name that cannot be broken into 2 lines
• makes vertical implementation almost impossible

```html
<!DOCTYPE html>
<html lang="en">
<head>
<meta charset="utf-8">
<title>VORAM (HK) Limited – Business Card</title>
<link href="https://fonts.googleapis.com/css2?family=Montserrat:wght@400;500;700&family=Noto+Sans+TC:wght@500&display=swap" rel="stylesheet">
<style>
  :root {
    --purple: #5a2479;
    --ink: #19181d;
    --paper: #ffffff;
    --stage: #2b2b2e;
  }
  * { box-sizing: border-box; margin: 0; padding: 0; }
  html, body { width: 1200px; height: 900px; overflow: hidden; }
  body {
    background: var(--stage);
    font-family: "Montserrat", Arial, sans-serif;
    display: flex; flex-direction: column; align-items: center; justify-content: center;
    gap: 50px;
  }
  .card {
    width: 600px; height: 343px; position: relative; overflow: hidden;
    box-shadow: 0 10px 30px rgba(0,0,0,.45);
  }
  /* Front */
  .card-front {
    background: var(--purple); color: var(--paper);
    display: flex; flex-direction: column; align-items: center; justify-content: center; gap: 14px;
  }
  .brand { display: flex; align-items: center; gap: 12px; }
  .brand-square { width: 26px; height: 26px; border-radius: 5px; background: currentColor; }
  .brand-name { font-weight: 700; font-size: 44px; letter-spacing: 4px; line-height: 1; }
  .company-front { font-size: 17px; font-weight: 400; letter-spacing: .5px; }
  /* Back */
  .card-back { background: var(--paper); }
  .back-top {
    position: absolute; left: 0; top: 0; width: 100%; height: 50%;
    display: flex; align-items: center; padding-left: 150px; gap: 28px; color: var(--purple);
  }
  .back-top .brand-name { font-size: 36px; }
  .back-top .brand-square { width: 22px; height: 22px; }
  .company-back { font-weight: 700; font-size: 19px; color: var(--purple); }
  .person {
    position: absolute; left: 0; bottom: 0; width: 53%; height: 50%;
    background: var(--ink); color: var(--paper);
    display: flex; flex-direction: column; align-items: center; justify-content: center; text-align: center;
  }
  .person-name { font-weight: 700; font-size: 24px; line-height: 1.15; }
  .person-name-zh { font-family: "Noto Sans TC", sans-serif; font-weight: 500; font-size: 22px; line-height: 1.2; }
  .credentials { font-weight: 700; font-size: 13px; margin-top: 3px; }
  .title { font-size: 12px; margin-top: 4px; }
  .contacts {
    position: absolute; right: 0; bottom: 0; width: 47%; height: 50%;
    background: var(--purple); color: var(--paper);
    display: flex; flex-direction: column; justify-content: center; gap: 9px; padding-left: 24px;
    list-style: none;
  }
  .contact { display: flex; align-items: center; gap: 12px; font-size: 11.5px; line-height: 1.3; }
  .contact-icon {
    flex: none; width: 26px; height: 26px; border-radius: 6px; background: var(--paper);
    display: flex; align-items: center; justify-content: center;
  }
  .contact-icon svg { width: 16px; height: 16px; fill: var(--purple); }
</style>
</head>
<body>
  <section class="card card-front" aria-label="Business card front">
    <div class="brand">
      <span class="brand-square"></span>
      <span class="brand-name">VORAM</span>
    </div>
    <p class="company-front">VORAM (HK) Limited</p>
  </section>

  <section class="card card-back" aria-label="Business card back">
    <div class="back-top">
      <div class="brand">
        <span class="brand-square"></span>
        <span class="brand-name">VORAM</span>
      </div>
      <p class="company-back">VORAM (HK) Limited</p>
    </div>

    <div class="person">
      <p class="person-name">Marcus L. Pryde</p>
      <p class="person-name-zh" lang="zh-Hant">林書恒</p>
      <p class="credentials">FCPA, FHKSI</p>
      <p class="title">Founder, Managing Director &amp; CEO</p>
    </div>

    <ul class="contacts">
      <li class="contact">
        <span class="contact-icon"><svg viewBox="0 0 24 24" aria-hidden="true"><path d="M6.6 10.8a15.1 15.1 0 0 0 6.6 6.6l2.2-2.2c.3-.3.7-.4 1-.2 1.1.4 2.3.6 3.6.6.6 0 1 .4 1 1V20c0 .6-.4 1-1 1A17 17 0 0 1 3 4c0-.6.4-1 1-1h3.5c.6 0 1 .4 1 1 0 1.3.2 2.5.6 3.6.1.3 0 .7-.2 1z"/></svg></span>
        <span>+852 3517 VORAM /<br>+852 3517 4062</span>
      </li>
      <li class="contact">
        <span class="contact-icon"><svg viewBox="0 0 24 24" aria-hidden="true"><path d="M8 1h8a2 2 0 0 1 2 2v18a2 2 0 0 1-2 2H8a2 2 0 0 1-2-2V3a2 2 0 0 1 2-2zm0 3v14h8V4zm4 15.5a1.2 1.2 0 1 0 0 2.4 1.2 1.2 0 0 0 0-2.4z"/></svg></span>
        <span>+852 6243 7719 /<br>+ 86 139 2745 3186</span>
      </li>
      <li class="contact">
        <span class="contact-icon"><svg viewBox="0 0 24 24" aria-hidden="true"><path d="M2 5h20v14H2zm2 2v.5l8 5.5 8-5.5V7zm0 2.9V17h16V9.9l-8 5.5z"/></svg></span>
        <span>marcus.l.pryde@voram-example.hk</span>
      </li>
    </ul>
  </section>
</body>
</html>
```